Business Card Design Project

Business card design for an IT Service company. A logo has already been created in a different contest and has been attached to this project. Ideally we're looking for a double sided business card that matches the look and feel of our newly created logo.

We're open to creativity if you feel a tag line is needed such as "IT Services and Application Development". We're open to really and look and feel - even single sided business cards if you feel you have something that's a great idea.

Last thought here - I'm not sure how it'll look but maybe a two tone card? One side dark blue and the other side white? Don't limit the design submissions to this tho - just curious if it would look good

Nothing too busy please - simple... Thank you and happy designing!

Target Market(s)

Businesses that require IT Services and support for hosted services, technical consultation, web design.

Industry/Entity Type

Business

Font styles to use
Sans Serif

Requirements
Must have
• Use the colors provided in the logo (see attachment) or additional colors that compliment
Must have the following contact info (not necessarily in this order):
- Owen Marsh
- Founding Partner
- omarsh@velomarquin.com
- 555-271-3948
- www.velomarquin.com

```html
<!DOCTYPE html>
<html lang="en">
<head>
<meta charset="utf-8">
<title>Velomarquin Business Card</title>
<link rel="stylesheet" href="https://fonts.googleapis.com/css2?family=Open+Sans:wght@400;700&family=Questrial&display=swap">
<style>
  :root {
    --backdrop: #e9e6e1;
    --card: #ffffff;
    --navy: #1d2a4f;
    --green: #3f7d31;
    --faint: #e4e8ee;
    --shadow: rgba(40, 35, 25, 0.18);
  }
  * { margin: 0; padding: 0; box-sizing: border-box; }
  html, body {
    width: 1200px;
    height: 870px;
    overflow: hidden;
    background: var(--backdrop);
  }
  .stage {
    position: relative;
    width: 1200px;
    height: 870px;
    display: flex;
    justify-content: center;
    align-items: center;
    gap: 80px;
  }
  .card {
    position: relative;
    width: 330px;
    height: 577px;
    background: var(--card);
    box-shadow: 0 10px 30px var(--shadow);
    font-family: "Open Sans", sans-serif;
    color: var(--navy);
  }
  .brand {
    position: absolute;
    display: flex;
    align-items: center;
    gap: 12px;
  }
  .brand-mark {
    width: 30px;
    height: 30px;
    background: var(--green);
  }
  .brand-name {
    font-family: "Open Sans", sans-serif;
    font-weight: 700;
    color: var(--navy);
    letter-spacing: -0.5px;
  }
  .card-front .brand { left: 26px; top: 92px; }
  .card-front .brand-name { font-size: 34px; }
  .person {
    position: absolute;
    left: 0; right: 0;
    top: 262px;
    text-align: center;
  }
  .person-name {
    font-family: "Questrial", sans-serif;
    font-size: 36px;
    line-height: 1.1;
    color: var(--navy);
  }
  .person-title {
    font-size: 17px;
    color: var(--green);
    margin-top: 2px;
  }
  .contact {
    position: absolute;
    left: 0; right: 0;
    top: 410px;
    list-style: none;
    text-align: center;
    font-size: 19px;
    line-height: 1.75;
    color: var(--navy);
  }
  .card-back .brand { left: 24px; top: 92px; }
  .card-back .brand-name { font-size: 34px; }
  .tagline {
    position: absolute;
    left: 24px;
    right: 20px;
    top: 172px;
    font-size: 14.5px;
    color: var(--green);
  }
  .back-accent {
    position: absolute;
    right: 28px;
    bottom: 36px;
    width: 150px;
    height: 150px;
    background: var(--faint);
  }
</style>
</head>
<body>
<main class="stage">
  <section class="card card-front" aria-label="Business card front">
    <div class="brand">
      <span class="brand-mark" aria-hidden="true"></span>
      <span class="brand-name">Velomarquin</span>
    </div>
    <div class="person">
      <h1 class="person-name">Owen Marsh</h1>
      <p class="person-title">Founding Partner</p>
    </div>
    <ul class="contact">
      <li class="contact-phone">555-271-3948</li>
      <li class="contact-email">omarsh@velomarquin.com</li>
      <li class="contact-web">www.velomarquin.com</li>
    </ul>
  </section>

  <section class="card card-back" aria-label="Business card back">
    <div class="brand">
      <span class="brand-mark" aria-hidden="true"></span>
      <span class="brand-name">Velomarquin</span>
    </div>
    <p class="tagline">IT Services and Application Development</p>
    <div class="back-accent" aria-hidden="true"></div>
  </section>
</main>
</body>
</html>
```